Business Card Design Project

Tall Pine Path- http:tallpinepath.com./rosalindkerr

Industry/Entity Type

Business

Contact Information for Business Card

Well it could be a pretty color like a glossy pink look business type very Job related

```html
<!DOCTYPE html>
<html lang="en">
<head>
<meta charset="UTF-8">
<title>Rosalind Kerr — Business Card</title>
<link href="https://fonts.googleapis.com/css2?family=Oswald:wght@200;300;600;700&family=Montserrat:wght@400;500&display=swap" rel="stylesheet">
<style>
  :root {
    --backdrop: #d9d9d9;
    --card-base: #b41f6c;
    --card-glow: #c63584;
    --band-bright: #d22478;
    --band-deep: #9c1a5e;
    --ink: #ffffff;
  }
  * { margin: 0; padding: 0; box-sizing: border-box; }
  html, body {
    width: 1200px;
    height: 800px;
    overflow: hidden;
    background: var(--backdrop);
  }
  .canvas {
    position: relative;
    width: 1200px;
    height: 800px;
    display: flex;
    align-items: center;
    justify-content: center;
  }
  .business-card {
    position: relative;
    width: 1050px;
    height: 600px;
    overflow: hidden;
    background:
      radial-gradient(ellipse 60% 70% at 42% 30%, var(--card-glow) 0%, rgba(198,53,132,0) 70%),
      var(--card-base);
    box-shadow: 0 6px 18px rgba(0,0,0,0.18);
  }
  .corner-bands {
    position: absolute;
    inset: 0;
    width: 100%;
    height: 100%;
  }
  .identity {
    position: absolute;
    right: 462px;
    top: 282px;
    display: flex;
    flex-direction: column;
    align-items: flex-end;
    color: var(--ink);
    white-space: nowrap;
  }
  .identity-name {
    font-family: "Oswald", sans-serif;
    font-size: 56px;
    line-height: 1;
    letter-spacing: 1px;
    text-transform: uppercase;
  }
  .name-first { font-weight: 200; }
  .name-last { font-weight: 600; }
  .identity-role {
    font-family: "Montserrat", sans-serif;
    font-weight: 400;
    font-size: 20px;
    line-height: 1.2;
    margin-top: 2px;
  }
  .divider {
    position: absolute;
    left: 620px;
    top: 200px;
    width: 2px;
    height: 176px;
    background: var(--ink);
  }
  .contact-list {
    position: absolute;
    left: 652px;
    top: 206px;
    list-style: none;
    color: var(--ink);
    font-family: "Montserrat", sans-serif;
    font-weight: 500;
    font-size: 20px;
    white-space: nowrap;
  }
  .contact-item {
    display: flex;
    align-items: center;
    gap: 12px;
    height: 30px;
  }
  .contact-icon {
    width: 18px;
    height: 18px;
    flex: none;
  }
</style>
</head>
<body>
<main class="canvas">
  <section class="business-card">
    <svg class="corner-bands" viewBox="0 0 1050 600" preserveAspectRatio="none" aria-hidden="true">
      <polygon points="380,600 1050,300 1050,380 520,600" fill="var(--band-bright)"/>
      <polygon points="520,600 1050,380 1050,600" fill="var(--band-deep)"/>
    </svg>

    <div class="identity">
      <h1 class="identity-name"><span class="name-first">Rosalind</span><span class="name-last">Kerr</span></h1>
      <p class="identity-role">Occupation</p>
    </div>

    <div class="divider"></div>

    <ul class="contact-list">
      <li class="contact-item">
        <svg class="contact-icon" viewBox="0 0 24 24" aria-hidden="true">
          <path fill="#fff" d="M6.6 10.8a15.1 15.1 0 0 0 6.6 6.6l2.2-2.2a1 1 0 0 1 1-.25 11.4 11.4 0 0 0 3.6.57 1 1 0 0 1 1 1V20a1 1 0 0 1-1 1A17 17 0 0 1 3 4a1 1 0 0 1 1-1h3.5a1 1 0 0 1 1 1c0 1.250.2 2.450.57 3.570a1 1 0 0 1-.25 1z"/>
        </svg>
        <span>000-000-0000</span>
      </li>
      <li class="contact-item">
        <svg class="contact-icon" viewBox="0 0 24 24" aria-hidden="true">
          <rect x="2.5" y="5" width="19" height="14" rx="1.5" fill="none" stroke="#fff" stroke-width="2"/>
          <path d="M3 6l9 7 9-7" fill="none" stroke="#fff" stroke-width="2"/>
        </svg>
        <span>info@tallpinepath.com</span>
      </li>
      <li class="contact-item">
        <svg class="contact-icon" viewBox="0 0 24 24" aria-hidden="true">
          <circle cx="12" cy="12" r="10" fill="#fff"/>
          <path d="M7 9c2 0 3 1 3 3s2 2 2 4M15 5c0 2 1 3 3 3" fill="none" stroke="var(--card-base)" stroke-width="1.8"/>
        </svg>
        <span>www.tallpinepath.com</span>
      </li>
    </ul>
  </section>
</main>
</body>
</html>
```